" Empresa de desenvolvimento humano, que trabalha principalmente a gestão dentro do ambiente de trabalho através de treinamento, consultoria e coaching. O principal conceito é que cada pessoa é única e seu auto-conhecimento é a chave para seu sucesso. "

```html
<!DOCTYPE html>
<html lang="pt-BR">
<head>
<meta charset="UTF-8">
<title>Veritas — Leadership and Engagement</title>
<link href="https://fonts.googleapis.com/css2?family=Montserrat:wght@300;400;500&display=swap" rel="stylesheet">
<style>
  :root {
    --page-bg: #e6e7e9;
    --brand-blue: #2c5f88;
    --brand-blue-deep: #1d4566;
    --photo-dark: #0e0f11;
    --photo-mid: #3a3c40;
    --band-bg: #f1f2f3;
    --band-line: #d6d8db;
    --text-dark: #5a5e63;
    --white: #ffffff;
  }
  * { margin: 0; padding: 0; box-sizing: border-box; }
  html, body {
    width: 1200px; height: 1200px; overflow: hidden;
    background: var(--page-bg);
    font-family: "Montserrat", sans-serif;
  }
  .screen {
    position: absolute; left: 40px; top: 285px;
    width: 1120px; height: 630px; overflow: hidden;
    background: var(--photo-dark);
  }
  .brand-panel {
    position: absolute; left: 0; top: 0; width: 480px; height: 100%;
    background: linear-gradient(160deg, var(--brand-blue) 0%, var(--brand-blue-deep) 100%);
  }
  .hero-photo {
    position: absolute; left: 480px; top: 0; right: 0; height: 100%;
    background:
      radial-gradient(ellipse at 70% 55%, rgba(200,200,205,0.35) 0%, rgba(0,0,0,0) 55%),
      linear-gradient(180deg, var(--photo-dark) 0%, var(--photo-mid) 60%, #1a1b1e 100%);
  }
  .brand-lockup {
    position: absolute; left: 0; width: 480px; top: 210px;
    text-align: center; color: var(--white);
  }
  .brand-name {
    font-weight: 300; font-size: 54px; letter-spacing: 4px; line-height: 1;
  }
  .brand-tagline {
    margin-top: 12px; font-weight: 400; font-size: 13px; letter-spacing: 4px;
    color: #c9d7e4;
  }
  .contact-band {
    position: absolute; left: 0; right: 0; top: 464px; height: 66px;
    background: var(--band-bg);
    border-top: 1px solid var(--band-line); border-bottom: 1px solid var(--band-line);
  }
  .contact-item {
    position: absolute; top: 12px; display: flex; align-items: center; gap: 14px;
    color: var(--text-dark); font-size: 11px; line-height: 1.4;
  }
  .contact-item--phone { left: 130px; }
  .contact-item--web { left: 425px; }
  .contact-item--address { left: 752px; }
  .contact-icon {
    width: 40px; height: 40px; border-radius: 6px; flex: none;
    background: var(--brand-blue);
    display: flex; align-items: center; justify-content: center;
  }
  .contact-icon svg { width: 22px; height: 22px; }
</style>
</head>
<body>
  <main class="screen">
    <section class="brand-panel">
      <div class="brand-lockup">
        <div class="brand-name">VERITAS</div>
        <div class="brand-tagline">LEADERSHIP AND ENGAGEMENT</div>
      </div>
    </section>
    <div class="hero-photo" role="img" aria-label="Dark photograph of a glowing financial bar chart on a digital grid"></div>

    <section class="contact-band">
      <div class="contact-item contact-item--phone">
        <span class="contact-icon">
          <svg viewBox="0 0 24 24" fill="none" stroke="#fff" stroke-width="2" stroke-linecap="round" stroke-linejoin="round"><path d="M22 16.9v3a2 2 0 0 1-2.2 2 19.8 19.8 0 0 1-8.6-3.1 19.5 19.5 0 0 1-6-6A19.8 19.8 0 0 1 2.1 4.2 2 2 0 0 1 4.1 2h3a2 2 0 0 1 2 1.7c.1.9.4 1.8.7 2.7a2 2 0 0 1-.5 2.1L8 9.8a16 16 0 0 0 6 6l1.3-1.3a2 2 0 0 1 2.1-.4c.9.3 1.8.6 2.7.7a2 2 0 0 1 1.7 2z"/></svg>
        </span>
        <span>+55 (11) 95555-0101<br>+55 (11) 3555-0102</span>
      </div>
      <div class="contact-item contact-item--web">
        <span class="contact-icon">
          <svg viewBox="0 0 24 24" fill="none" stroke="#fff" stroke-width="2"><circle cx="12" cy="12" r="10"/><path d="M2 12h20M12 2a15 15 0 0 1 0 20M12 2a15 15 0 0 0 0 20"/></svg>
        </span>
        <span>contato@veritasdh.com.br<br>www.veritasdh.com.br</span>
      </div>
      <div class="contact-item contact-item--address">
        <span class="contact-icon">
          <svg viewBox="0 0 24 24" fill="#fff"><path d="M12 2a7 7 0 0 0-7 7c0 5.2 7 13 7 13s7-7.8 7-13a7 7 0 0 0-7-7zm0 9.5A2.5 2.5 0 1 1 12 6.5a2.5 2.5 0 0 1 0 5z"/></svg>
        </span>
        <span>Rua das Acácias, 240<br>Bairro Jardim Aurora<br>04100-000 - São Paulo / SP</span>
      </div>
    </section>
  </main>
</body>
</html>
```